Detailing informational flyer

I want to design a new flyer for my automotive detailing business. The flyer should use the color scheme from the logo and be easy to read and understand the services we offer.

Font styles to use
Serif
Sans Serif

Colors
3176b5
0255a3
fbed22
33a6d7
0692cd
ffffff

Requirements
Must have
• must include all information from the copy
Nice to have
• include a Glenvaro logo such as the image attached

```html
<!DOCTYPE html>
<html lang="en">
<head>
<meta charset="utf-8">
<title>Detail Center – Ridgeway Carwash</title>
<link href="https://fonts.googleapis.com/css2?family=Ubuntu:wght@400;500;700&display=swap" rel="stylesheet">
<style>
  :root {
    --navy: #0d2a66;
    --royal: #0255a3;
    --steel: #3176b5;
    --sky: #33a6d7;
    --cyan: #0692cd;
    --yellow: #fbed22;
    --gold: #f5d63a;
    --white: #ffffff;
    --ink: #1b2a4a;
    --title-blue: #5b97d6;
    --icon-bg: #123a85;
  }
  * { margin: 0; padding: 0; box-sizing: border-box; }
  html, body { width: 860px; height: 1200px; overflow: hidden; background: #d9d9d9; }
  .flyer {
    position: relative; width: 860px; height: 1200px; overflow: hidden;
    background: radial-gradient(ellipse at 60% 75%, #1e4fa0 0%, var(--navy) 70%);
    font-family: "Ubuntu", sans-serif; color: var(--white);
  }
  .hero { position: absolute; left: 0; top: 0; width: 860px; height: 500px; }
  .service-line {
    position: absolute; top: 30px; left: 0; width: 860px; text-align: center;
    color: var(--yellow); font-weight: 700; font-size: 22px; letter-spacing: 0.6px;
  }
  .brand { position: absolute; left: 30px; top: 496px; }
  .brand-title {
    font-weight: 700; font-size: 58px; color: var(--title-blue); letter-spacing: 0.5px;
    text-shadow: 0 3px 4px rgba(0,0,0,0.45); line-height: 1;
  }
  .brand-sub {
    margin-top: 12px; margin-left: 8px; font-weight: 700; font-size: 30px;
    color: var(--yellow); letter-spacing: 8px; line-height: 1;
  }
  .service-icon { position: absolute; left: 24px; width: 98px; height: 98px; }
  .service-text {
    position: absolute; left: 151px; width: 680px;
    font-size: 15.4px; line-height: 17.8px; text-align: justify;
  }
  .service-text strong { color: var(--yellow); font-weight: 700; }
  .note {
    position: absolute; left: 23px; top: 1072px; color: var(--yellow);
    font-weight: 700; font-size: 17px;
  }
  .partner {
    position: absolute; left: 716px; top: 1069px; color: var(--yellow);
    font-weight: 700; font-size: 22px; letter-spacing: 0.5px;
  }
  .footer-band {
    position: absolute; left: 0; top: 1142px; width: 860px; height: 58px;
    background: var(--yellow);
  }
  .address {
    position: absolute; left: 0; top: 1163px; width: 860px; text-align: center;
    color: var(--ink); font-weight: 700; font-size: 22px; letter-spacing: 0.8px;
  }
  .phone {
    position: absolute; left: 249px; top: 1110px; width: 366px; height: 50px;
    border-radius: 25px;
    background: linear-gradient(180deg, #4ab8ec 0%, var(--cyan) 55%, var(--steel) 100%);
    box-shadow: 0 3px 6px rgba(0,0,0,0.35);
    display: flex; align-items: center; justify-content: center; gap: 14px;
    color: var(--yellow); font-weight: 700; font-size: 28px;
  }
  .phone svg { width: 34px; height: 34px; }
</style>
</head>
<body>
<div class="flyer">

  <svg class="hero" viewBox="0 0 860 500">
    <defs>
      <radialGradient id="heroGlow" cx="55%" cy="35%" r="70%">
        <stop offset="0" stop-color="#7cc8f0"/>
        <stop offset="0.45" stop-color="#2a8fd6"/>
        <stop offset="1" stop-color="#0a3f95"/>
      </radialGradient>
      <linearGradient id="photoTone" x1="0" y1="0" x2="1" y2="1">
        <stop offset="0" stop-color="#3b86d4"/>
        <stop offset="0.5" stop-color="#2460b3"/>
        <stop offset="1" stop-color="#7fc6ea"/>
      </linearGradient>
      <linearGradient id="emblemTone" x1="0" y1="0" x2="1" y2="0">
        <stop offset="0" stop-color="#6aa6dc"/>
        <stop offset="0.35" stop-color="#f2dc45"/>
        <stop offset="1" stop-color="#f2dc45"/>
      </linearGradient>
    </defs>
    <rect width="860" height="500" fill="var(--royal)"/>
    <path d="M0 0 H860 V385 C760 430 620 470 480 475 C330 480 180 440 0 430 Z" fill="url(#heroGlow)"/>
    <path role="img" aria-label="Photo of a blue sports car splashing through water"
          d="M150 300 C190 230 300 175 460 168 C640 160 790 200 860 240 V392 C760 432 620 462 480 462 C360 462 240 440 150 410 Z"
          fill="url(#photoTone)" opacity="0.9"/>
    <path d="M0 436 C180 447 330 487 480 482 C620 477 760 437 860 392 V500 H0 Z" fill="var(--navy)"/>
    <path d="M0 430 C180 440 330 480 480 475 C620 470 760 430 860 385"
          fill="none" stroke="var(--gold)" stroke-width="12"/>
    <path role="img" aria-label="Carwash emblem illustration of a yellow sports car with blue bubbles"
          d="M70 470 C70 400 110 330 170 300 C240 330 320 350 380 380 C420 395 438 430 432 470 C330 488 170 490 70 470 Z"
          fill="url(#emblemTone)"/>
  </svg>

  <div class="service-line">CAR WASH · OIL LUBE &amp; FILTER SERVICE · AUTO DETAILING SERVICE</div>

  <div class="brand">
    <div class="brand-title">DETAIL CENTER</div>
    <div class="brand-sub">RIDGEWAY CARWASH</div>
  </div>

  <svg class="service-icon" style="top:607px" viewBox="0 0 100 100" role="img" aria-label="Car wash icon">
    <circle cx="50" cy="46" r="44" fill="var(--icon-bg)"/>
    <path d="M3 55 A47 47 0 0 0 97 55" fill="none" stroke="var(--yellow)" stroke-width="2.5"/>
    <circle cx="50" cy="46" r="20" fill="var(--yellow)"/>
  </svg>
  <p class="service-text" style="top:627px"><strong>EXTERIOR DETAILING INCLUDES:</strong> We wash, clay, compound, polish, and wax, as needed to restore the deep rich gloss and provide a durable shine for that “new car” look. This process removes light oxidation from the vehicle and protects the clear coat finish. Finishing touches include rim cleaning and tire shine.</p>

  <svg class="service-icon" style="top:724px" viewBox="0 0 100 100" role="img" aria-label="Interior seat cleaning icon">
    <circle cx="50" cy="46" r="44" fill="var(--icon-bg)"/>
    <path d="M3 55 A47 47 0 0 0 97 55" fill="none" stroke="var(--yellow)" stroke-width="2.5"/>
    <circle cx="50" cy="46" r="20" fill="var(--yellow)"/>
  </svg>
  <p class="service-text" style="top:727px"><strong>INTERIOR DETAILING SHAMPOO INCLUDES:</strong> We perform a deep cleaning of the interior such as the dashboard, door jams, center console, trunk area, upholstered seats, andall carpets and mats. This process will remove soils and most stains. Windows are cleaned inside and out. All leather is dressed to provide a protective finish. Air fresher is available upon request.</p>

  <svg class="service-icon" style="top:841px" viewBox="0 0 100 100" role="img" aria-label="Wheel polishing icon">
    <circle cx="50" cy="46" r="44" fill="var(--icon-bg)"/>
    <path d="M3 55 A47 47 0 0 0 97 55" fill="none" stroke="var(--yellow)" stroke-width="2.5"/>
    <circle cx="50" cy="46" r="20" fill="var(--yellow)"/>
  </svg>
  <p class="service-text" style="top:841px"><strong>MINI DETAIL/ VIP SERVICE INCLUDES:</strong> Ridgeway Special Wash with triple polish wax, Glenvaro Shield protectant, tire shine, and a detailed and gentle cleaning of the upholstery. 4 rubber or carpet mats are shampooed. All interior surfaces are dressed including dashboard, door panels, center console. This is followed by a detailed carpet and upholstery vacuum with compressed air to remove dirt from hard to reach places. For added shine ask about adding on our express wax service to your mini detail package.</p>

  <svg class="service-icon" style="top:962px" viewBox="0 0 100 100" role="img" aria-label="Headlight restoration icon">
    <circle cx="50" cy="46" r="44" fill="var(--icon-bg)"/>
    <path d="M3 55 A47 47 0 0 0 97 55" fill="none" stroke="var(--yellow)" stroke-width="2.5"/>
    <circle cx="50" cy="46" r="20" fill="var(--yellow)"/>
  </svg>
  <p class="service-text" style="top:992px"><strong>HEADLIGHT RESTORATION:</strong> This shop proudly offers the Headlight Service, which can polish or restore your headlight to a clear, safe condition at a fraction of the cost of headlight replacement! Restore the lens to a clear, shiny &amp; safe condition.</p>

  <p class="note">Ask to speak to a manager about scheduling any of our detailing services.</p>
  <div class="partner">GLENVARO</div>

  <div class="footer-band"></div>
  <div class="phone">
    <svg viewBox="0 0 34 34" aria-hidden="true">
      <circle cx="17" cy="17" r="14" fill="none" stroke="var(--yellow)" stroke-width="2.5"/>
      <path d="M12 10 l3 0 l1.5 4 l-2 1.5 c1 2.2 2.6 3.8 4.8 4.8 l1.5 -2 l4 1.5 l0 3 c-7 0.5 -13.3 -5.8 -12.8 -12.8 z" fill="var(--yellow)"/>
    </svg>
    <span>+1 555-013-4720</span>
  </div>
  <div class="address">48-20 Larkmont Ave Elm Gardens 10482</div>

</div>
</body>
</html>
```